Flyer-Design für Wohungsvermietung
Zielgruppe
Ich vermiete in einer Neubausiedlung 'Rosenhang Feldbrück' Wohnungen und möchte gerne für die Erstvermietung einen Flyer erstellen lassen, welchen wir in der Region aushängen bzw. abgeben können.
Aufgabenstellung
Flyer sollte über das Format A5 verfügen und auf beiden Seiten bedruckbar sein. Die Grafik sollte ansprechend für alle Altergruppen sein. Auf den Ersten Blick sollten alle wichtige Informationen ersichtlich sein. Es handelt sich um hochwertige Mietwohnungen mit einer ausgezeichneten Aussicht auf die Alpen. Die Schule befindet sich gleich anschliessend an die neue Siedlung. Ausführliche Informationen gibt es bereits auf einer Webseite: https://www.rosenhang-feldbrueck-wohnen.ch

```html
<!DOCTYPE html>
<html lang="de">
<head>
<meta charset="utf-8">
<title>Rosenhang Feldbrück – Flyer</title>
<link href="https://fonts.googleapis.com/css2?family=Kaushan+Script&family=Open+Sans:wght@400;600;700&display=swap" rel="stylesheet">
<style>
  :root {
    --brand-red: #a3192f;
    --brand-gray: #45474a;
    --sun-yellow: #f2c21b;
    --paper: #ffffff;
    --stage: #ece9e7;
    --text: #2b2b2b;
  }
  * { box-sizing: border-box; margin: 0; padding: 0; }
  html, body { width: 1200px; height: 1200px; overflow: hidden; }
  body {
    background: var(--stage);
    font-family: "Open Sans", Arial, sans-serif;
    color: var(--text);
    position: relative;
  }
  .flyer {
    position: absolute;
    left: 190px;
    width: 820px;
    height: 550px;
    background: var(--paper);
    overflow: hidden;
    box-shadow: 0 6px 24px rgba(0,0,0,.18);
  }
  .flyer--front { top: 34px; }
  .flyer--back { top: 616px; }

  /* Front */
  .front-photo {
    position: absolute; inset: 0;
    background:
      linear-gradient(180deg, rgba(255,255,255,.0) 0%, rgba(0,0,0,.0) 45%, rgba(20,12,10,.55) 100%),
      linear-gradient(100deg, #d9dde2 0%, #b8bfc7 30%, #6e6a66 55%, #3b2b24 75%, #2a1c18 100%);
  }
  .front-photo__accent {
    position: absolute; right: 0; bottom: 0; width: 38%; height: 48%;
    background: radial-gradient(ellipse at 60% 60%, #8c1d2c 0%, #5a1620 55%, rgba(60,20,24,0) 80%);
  }
  .front-headline {
    position: absolute; left: 44px; top: 52px;
    font-family: "Kaushan Script", cursive;
    color: var(--brand-red);
    font-size: 44px; line-height: 1.22;
    transform: rotate(-8deg);
    transform-origin: left top;
  }
  .front-headline span { display: block; }
  .front-headline span:nth-child(2) { margin-left: 6px; }
  .front-headline span:nth-child(3) { margin-left: 14px; }
  .logo-box {
    position: absolute; right: 0; top: 30px;
    width: 240px; height: 102px;
    background: rgba(255,255,255,.92);
    padding: 6px;
  }
  .logo-box__inner {
    border: 1.5px dashed var(--brand-red);
    height: 100%;
    display: flex; align-items: center; justify-content: center; gap: 8px;
  }
  .brand-mark { display: flex; align-items: center; gap: 8px; }
  .brand-mark__dot { width: 14px; height: 14px; border-radius: 50%; background: var(--sun-yellow); flex: none; }
  .brand-mark__name {
    font-weight: 600; color: var(--brand-red);
    font-size: 17px; letter-spacing: .5px;
  }
  .front-link {
    position: absolute; left: 44px; bottom: 44px;
    color: #fff; font-weight: 600; font-size: 13px;
  }

  /* Back */
  .back-photo {
    position: absolute; left: 0; top: 0; width: 100%; height: 198px;
    background: linear-gradient(180deg, #dfe4e8 0%, #b9c7b4 22%, #7f9a5f 45%, #8a9a6d 65%, #b49a83 85%, #9ea49a 100%);
  }
  .back-headline {
    position: absolute; left: 50px; top: 216px;
    font-family: "Kaushan Script", cursive;
    color: var(--brand-red); font-size: 14.5px;
  }
  .back-columns {
    position: absolute; left: 50px; top: 256px;
    width: 500px;
    column-count: 2; column-gap: 12px;
    font-size: 9.6px; line-height: 1.42;
    text-align: justify;
  }
  .back-columns p { margin-bottom: 10px; }
  .back-columns .lead { font-weight: 700; }
  .back-contact {
    position: absolute; left: 590px; top: 256px; width: 190px;
    font-size: 9.6px; line-height: 1.42;
  }
  .back-contact p { margin-bottom: 9px; }
  .back-contact .strong { font-weight: 600; }
  .back-contact .signoff {
    font-family: "Kaushan Script", cursive;
    color: var(--brand-red); font-size: 11px;
  }
  .interior-strip {
    position: absolute; left: 0; bottom: 0; height: 96px; width: 550px;
    display: flex; gap: 4px; background: var(--brand-red);
    border-right: 4px solid var(--brand-red);
  }
  .interior-strip__photo {
    flex: 1;
    background: linear-gradient(90deg, #e9ebe8 0%, #c9cfc8 40%, #a98e73 80%, #8d7760 100%);
  }
  .interior-strip__photo--kitchen {
    background: linear-gradient(90deg, #f2f2f0 0%, #d8dad6 45%, #8fb27d 75%, #b09273 100%);
  }
  .back-logo {
    position: absolute; right: 40px; bottom: 30px;
  }
  .back-logo .brand-mark__name { font-size: 15px; }
</style>
</head>
<body>

<section class="flyer flyer--front">
  <div class="front-photo" role="img" aria-label="Foto: warme Stube mit Blick aus dem Fenster auf verschneite Berge, Kaffeetasse auf dem Fensterbrett und Füße in roten Wollsocken">
    <div class="front-photo__accent"></div>
  </div>
  <h1 class="front-headline">
    <span>Jeden Morgen mit</span>
    <span>einem Ausblick beginnen</span>
    <span>der begeistert.</span>
  </h1>
  <div class="logo-box">
    <div class="logo-box__inner">
      <div class="brand-mark">
        <span class="brand-mark__dot"></span>
        <span class="brand-mark__name">Rosenhang Feldbrück</span>
      </div>
    </div>
  </div>
  <p class="front-link">Mehr unter: www.rosenhang-feldbrueck-wohnen.ch</p>
</section>

<section class="flyer flyer--back">
  <div class="back-photo" role="img" aria-label="Foto: Blick über Dächer und grüne Felder bis zu Wäldern und Hügeln"></div>
  <h2 class="back-headline">Daheim im Rosenhang Feldbrück vermieten wir per sofort 3.5 bis 5.5 Zimmer Wohnungen.</h2>
  <div class="back-columns">
    <p class="lead">Eingebettet in die reizvolle Landschaft am Südhang des Hohenwaldberges liegt Feldbrück. Die ideale Lage und die wunderbare Aussicht auf das Alpenpanorama machen das Dorf zu dem Ort, an dem man immer wieder gerne zurückkehrt: zum eigenen Zuhause.</p>
    <p>Mit der Nähe zu Bern und der Autobahn sind Einkaufsmöglichkeiten, Freizeitgestaltung und Arbeitsstellen schnell mit dem Auto oder den öffentlichen Verkehrsmitteln erreicht.<br>Die beiden Mehrfamilienhäuser bieten helle, sonnige Wohnungen mit Ausrichtung gegen Süden. Die beiden Gartenwohnungen zeichnet ein abgeschlossener Wohngarten aus und von den großzügigen Attikawohnungen genießt man den ungehinderten Blick in die Alpen. Private Parkplätze, das Kellergeschoss, große Balkone, eigene Waschräume und ein Lift sind nur einige der zu nennenden Eigenschaften der Wohnungen. Der Außenbereich bietet einen Garten zum Entspannen und einen Abenteuerspielplatz für die jungen Bewohner unter uns. Der Gehweg ins Dorf und ins Schulhaus ist ebenfalls direkt am Grundstück angeschlossen und führt innerhalb weniger Minuten ins Zentrum.</p>
  </div>
  <div class="back-contact">
    <p class="strong">Wir haben Ihr Interesse geweckt?</p>
    <p class="strong">Dann besuchen Sie gern unsere Internetseite:<br>www.rosenhang-feldbrueck-wohnen.ch</p>
    <p class="strong">Oder rufen Sie uns für weitere Auskünfte direkt an unter:<br>031 555 08 12</p>
    <p>Wir freuen uns auf ein baldiges Kennenlernen</p>
    <p class="signoff">Ihr Team vom Rosenhang Feldbrück</p>
  </div>
  <div class="interior-strip">
    <div class="interior-strip__photo" role="img" aria-label="Foto: heller Wohnraum mit Parkett und großen Fenstern"></div>
    <div class="interior-strip__photo interior-strip__photo--kitchen" role="img" aria-label="Foto: offene Küche mit Fensterfront zum Garten"></div>
  </div>
  <div class="back-logo brand-mark">
    <span class="brand-mark__dot"></span>
    <span class="brand-mark__name">Rosenhang Feldbrück</span>
  </div>
</section>

</body>
</html>
```